Conceptual Model Diagram for Replacing Medication with Behavior to Support Weight Loss Maintenance

Design a figure of a conceptual model that needs to be inserted into a word document for a PSF grant. This conceptual model illustrates how behavioral strategies can replace the regulatory functions lost after AOM discontinuation. The intervention targets three core vulnerabilities—appetite resurgence, metabolic inflexibility, and suboptimal mindstate—through the domains of Food, Physical Activity, and Mind. Sustained weight loss maintenance occurs at the intersection of these domains. The intervention is delivered within a design framework that makes behaviors easier to perform, aligns them with identity, and reinforces them through virtual support and community, ensuring real-world feasibility and long-term adherence.
Target Market(s)
PSF reviewers
Industry/Entity Type
academic
Other font styles liked:
- arial
Requirements
Must have
- see my attached description

```html
<!DOCTYPE html>
<html lang="en">
<head>
<meta charset="utf-8">
<title>Conceptual Model: Behavior Replacing Medication for Weight Loss Maintenance</title>
<link rel="stylesheet" href="https://fonts.googleapis.com/css2?family=Arimo:wght@700&family=Alfa+Slab+One&family=Roboto+Condensed:wght@600&display=swap">
<style>
  :root {
    --teal: #22a0a6;
    --teal-dark: #1e878b;
    --line-blue: #0d7aa3;
    --ink-teal: #1d8388;
    --paper: #ffffff;
    --page: #ffffff;
  }
  html, body {
    margin: 0;
    padding: 0;
    width: 1176px;
    height: 1200px;
    overflow: hidden;
    background: var(--page);
  }
  .model { display: block; width: 1176px; height: 1200px; }
  .card { fill: var(--paper); filter: drop-shadow(6px 6px 5px rgba(0,0,0,0.45)); }
  .frame { fill: none; stroke: var(--line-blue); stroke-width: 5; }
  .box-light { fill: var(--teal); }
  .box-dark { fill: var(--teal-dark); }
  .connector { fill: none; stroke: var(--line-blue); stroke-width: 7; }
  .arrow-head { fill: var(--line-blue); }
  .drop-arrow { fill: var(--teal); }
  .sans { font-family: "Arimo", Arial, sans-serif; font-weight: 700; fill: #fff; }
  .condensed { font-family: "Roboto Condensed", "Arial Narrow", sans-serif; font-weight: 600; fill: #fff; }
  .slab { font-family: "Alfa Slab One", "Rockwell", serif; fill: #fff; }
  .heading-teal { fill: var(--ink-teal); }
  .domain-light { fill: var(--teal); stroke: #fff; stroke-width: 6; }
  .domain-dark { fill: var(--teal-dark); stroke: #fff; stroke-width: 4; stroke-linejoin: round; }
</style>
</head>
<body>
<svg class="model" viewBox="0 0 1903 1942" preserveAspectRatio="none" xmlns="http://www.w3.org/2000/svg" role="img" aria-label="Conceptual model of behavioral strategies for weight loss maintenance after AOM discontinuation">
  <rect class="card" x="380" y="190" width="1215" height="1562"/>
  <rect class="frame" x="410" y="212" width="1152" height="1508"/>

  <!-- Premise -->
  <rect class="box-light" x="447" y="252" width="1075" height="158" rx="40"/>
  <text class="sans" font-size="51" text-anchor="middle">
    <tspan x="985" y="317">Behavioral strategies replace regulatory</tspan>
    <tspan x="985" y="377">function lost after AOM discontinuation</tspan>
  </text>

  <!-- Drop arrows -->
  <g class="drop-arrow">
    <path d="M576 410 H606 V437 H624 L591 470 L558 437 H576 Z"/>
    <path d="M970 410 H1000 V437 H1018 L985 470 L952 437 H970 Z"/>
    <path d="M1363 410 H1393 V437 H1411 L1378 470 L1345 437 H1363 Z"/>
  </g>

  <!-- Vulnerabilities -->
  <rect class="box-dark" x="447" y="470" width="330" height="130" rx="30"/>
  <rect class="box-dark" x="818" y="470" width="330" height="130" rx="30"/>
  <rect class="box-light" x="1192" y="470" width="330" height="130" rx="30"/>
  <text class="sans" font-size="50" text-anchor="middle">
    <tspan x="617" y="527">Appetite</tspan><tspan x="617" y="580">Resurgence</tspan>
    <tspan x="985" y="527">Metabolic</tspan><tspan x="985" y="580">Inflexibility</tspan>
    <tspan x="1360" y="527">Suboptimal</tspan><tspan x="1360" y="580">Mindstate</tspan>
  </text>

  <!-- Connectors -->
  <path class="connector" d="M591 612 V648 Q591 662 605 662 H717 Q731 662 731 676 V706"/>
  <path class="arrow-head" d="M712 704 H750 L731 727 Z"/>
  <path class="connector" d="M983 612 V648 Q983 662 969 662 H881 Q867 662 867 676 V706"/>
  <path class="arrow-head" d="M848 704 H886 L867 727 Z"/>
  <path class="connector" d="M1371 612 V645 Q1371 668 1345 668 H1128 Q1098 668 1098 698 V1450 Q1098 1477 1125 1477 H1522"/>

  <!-- Domains -->
  <circle class="domain-light" cx="670" cy="1145" r="187"/>
  <circle class="domain-light" cx="938" cy="1145" r="187"/>
  <path class="domain-dark" d="M623 962 A185 185 0 1 1 987 962 Z"/>
  <path class="domain-dark" d="M620 963 L992 963 L805 1280 Z"/>

  <text class="slab" font-size="52" text-anchor="middle" x="800" y="897">Mind</text>
  <text class="slab" font-size="30" text-anchor="middle">
    <tspan x="805" y="1004">Sustained</tspan>
    <tspan x="805" y="1041">Weight Loss</tspan>
    <tspan x="805" y="1078">Maintenance</tspan>
  </text>
  <text class="slab" font-size="50" text-anchor="middle" x="603" y="1193">Food</text>
  <text class="slab" font-size="43" text-anchor="middle">
    <tspan x="998" y="1165">Physical</tspan>
    <tspan x="995" y="1215">Activity</tspan>
  </text>

  <!-- Design framework -->
  <text class="sans heading-teal" font-size="42">
    <tspan x="1170" y="749">Intervention</tspan>
    <tspan x="1170" y="798">delivered within a</tspan>
    <tspan x="1170" y="847">design framework</tspan>
    <tspan x="1170" y="896">that</tspan>
  </text>
  <rect class="box-light" x="1165" y="936" width="357" height="122" rx="28"/>
  <rect class="box-light" x="1165" y="1082" width="357" height="121" rx="28"/>
  <rect class="box-light" x="1167" y="1228" width="353" height="215" rx="28"/>
  <text class="sans" font-size="35">
    <tspan x="1189" y="988">Makes behaviors</tspan>
    <tspan x="1189" y="1030">easier to perform</tspan>
  </text>
  <text class="sans" font-size="35" text-anchor="middle">
    <tspan x="1338" y="1134">Aligns them</tspan>
    <tspan x="1338" y="1176">with identity</tspan>
  </text>
  <text class="sans" font-size="35">
    <tspan x="1189" y="1288">Reinforces them</tspan>
    <tspan x="1189" y="1330">through virtual</tspan>
    <tspan x="1189" y="1372">support and</tspan>
    <tspan x="1189" y="1414">community</tspan>
  </text>

  <!-- Upward connectors -->
  <path class="connector" d="M800 1497 V1460 Q800 1440 780 1440 H680 Q661 1440 661 1421 V1382"/>
  <path class="connector" d="M800 1460 Q800 1440 820 1440 H922 Q941 1440 941 1421 V1382"/>
  <path class="arrow-head" d="M642 1384 H680 L661 1360 Z"/>
  <path class="arrow-head" d="M922 1384 H960 L941 1360 Z"/>

  <!-- Summary -->
  <rect class="box-light" x="432" y="1497" width="1111" height="195" rx="45"/>
  <text class="condensed" font-size="51" text-anchor="middle">
    <tspan x="990" y="1547">Targets three core vulnerabilities through the</tspan>
    <tspan x="990" y="1607">domains od Food, Physical Activity, and Mind</tspan>
    <tspan x="990" y="1667">ensuring real-world feasibility and community</tspan>
  </text>
</svg>
</body>
</html>
```